3" Round Business Card for Funeral Home

We need a business card designed for our cremation service. We would like to use a 3" round business card.

The business card will be 2-sided. One side with the logo featured prominently. The back sad will have employee name and contact info.

Templates for printing have been attached to project as well as logo

We like soft colors like the logo. Final design should promote a feeling of trust.

Industry/Entity Type

Funeral

Contact Information for Business Card

Employee Name, Phone number, email, web address

Requirements
Should not have
• any sort of funeral item such as urn, casket, hearse, tombstone

```html
<!DOCTYPE html>
<html lang="en">
<head>
<meta charset="utf-8">
<title>Ashgrove Care – Round Business Card</title>
<link href="https://fonts.googleapis.com/css2?family=Montserrat:wght@300;400;600;700&display=swap" rel="stylesheet">
<style>
  :root {
    --bg: #dedede;
    --card-white: #fbfbfb;
    --purple: #8e2d8e;
    --teal: #1fa39a;
    --ink: #3a3a3a;
  }
  html, body {
    margin: 0;
    padding: 0;
    width: 1200px;
    height: 1059px;
    overflow: hidden;
    background: var(--bg);
    font-family: "Montserrat", sans-serif;
  }
  .canvas { position: relative; width: 1200px; height: 1059px; }
  .card {
    position: absolute;
    top: 260px;
    width: 530px;
    height: 530px;
    border-radius: 50%;
  }
  .card--back { left: 42px; background: var(--card-white); }
  .card--front { left: 629px; background: var(--purple); }

  .brand {
    position: absolute;
    left: 0; right: 0;
    text-align: center;
    font-weight: 400;
    letter-spacing: -0.5px;
    line-height: 1;
  }
  .card--back .brand { top: 112px; font-size: 44px; color: var(--teal); }
  .card--front .brand { top: 228px; font-size: 56px; color: #fff; }

  .person { position: absolute; left: 0; right: 0; text-align: center; }
  .person__name {
    top: 218px;
    font-size: 21px;
    font-weight: 700;
    letter-spacing: 1px;
    color: var(--teal);
  }
  .person__role { top: 244px; font-size: 15px; color: var(--ink); letter-spacing: 0.5px; }

  .divider { position: absolute; left: 166px; width: 198px; top: 280px; height: 20px; }
  .divider--plain { top: 379px; height: 2px; }

  .details {
    position: absolute;
    left: 0; right: 0;
    margin: 0;
    text-align: center;
    font-size: 15.5px;
    line-height: 20px;
    color: var(--ink);
    letter-spacing: 0.4px;
  }
  .details--contact { top: 305px; }
  .details--address { top: 390px; }
</style>
</head>
<body>
<main class="canvas">
  <section class="card card--back" aria-label="Card back with contact details">
    <div class="brand">ashgrovecare</div>
    <div class="person person__name">DANIEL WHITCOMBE</div>
    <div class="person person__role">Managing Director</div>

    <svg class="divider" viewBox="0 0 198 20" aria-hidden="true">
      <line x1="0" y1="10" x2="60" y2="10" stroke="var(--purple)" stroke-width="1"/>
      <line x1="138" y1="10" x2="198" y2="10" stroke="var(--purple)" stroke-width="1"/>
      <circle cx="75" cy="10" r="9" fill="var(--teal)"/>
      <path d="M71 6 q1-1 2 0 l1 2 q0 1-1 1.5 q1 2 3 3 q0.5-1 1.5-1 l2 1 q1 1 0 2 q-1 1-3 0.5 q-5-2-6.5-7 q-0.3-1.5 1-2z" fill="#fff"/>
      <circle cx="99" cy="10" r="9" fill="var(--teal)"/>
      <rect x="94" y="6.5" width="10" height="7" rx="1" fill="#fff"/>
      <path d="M94 7 l5 4 l5-4" fill="none" stroke="var(--teal)" stroke-width="1"/>
      <circle cx="123" cy="10" r="9" fill="var(--teal)"/>
      <circle cx="123" cy="10" r="5" fill="none" stroke="#fff" stroke-width="1.3"/>
      <path d="M118 10 h10 M123 5 v10" stroke="#fff" stroke-width="1"/>
    </svg>

    <p class="details details--contact">555-210-7734<br>hello@ashgrovecare.com<br>www.ashgrovecare.com</p>
    <svg class="divider divider--plain" viewBox="0 0 198 2" aria-hidden="true">
      <line x1="0" y1="1" x2="198" y2="1" stroke="var(--purple)" stroke-width="1"/>
    </svg>
    <p class="details details--address">1480 W Maple Avenue<br>Harlow County name 6142</p>
  </section>

  <section class="card card--front" aria-label="Card front with brand name">
    <div class="brand">ashgrovecare</div>
  </section>
</main>
</body>
</html>
```